After tattoo calming solution

The label has to be modern, along the same lines as skin care brand “Dew Harbor.” It has to reflect the solutions natural effectiveness and simplicity. The label cannot be over fussy, and must be a little bit clinical, as it really does work. The colours should reflect that the solution calms the skin.

We use a 100ml spray bottle.

Target Market(s)

Anyone with a new tattoo or piercing

Industry/Entity Type

Skincare

Requirements
Must have
• Must reflect its natural calming but still remain a little clinical
Should not have
• It must not look like other flowery tattoo cream solutions.

```html
<!DOCTYPE html>
<html lang="en">
<head>
<meta charset="UTF-8">
<title>After Tattoo &amp; Piercing – 100 mL Label</title>
<link rel="stylesheet" href="https://fonts.googleapis.com/css2?family=PT+Serif:wght@400;700&family=Josefin+Sans:wght@300;400&family=Oswald:wght@600&display=swap">
<style>
  :root {
    --page: #ffffff;
    --label-bg: #fcf3ee;
    --rose: #d06fa3;
    --coral: #ea9e84;
    --peach-band: #f0b096;
    --peach-fill: #fbe6da;
    --rule: #f3c3a8;
    --ink: #3f3f3f;
  }
  * { margin: 0; padding: 0; box-sizing: border-box; }
  html, body {
    width: 1200px;
    height: 1000px;
    overflow: hidden;
    background: var(--page);
  }
  .label {
    position: absolute;
    left: 365px;
    top: 96px;
    width: 471px;
    height: 808px;
    background: var(--label-bg);
    overflow: hidden;
  }
  .rule {
    position: absolute;
    left: 52px;
    width: 372px;
    height: 8px;
    border-radius: 50%;
    background: radial-gradient(ellipse at center, var(--rule) 0%, rgba(243,195,168,0.7) 45%, rgba(243,195,168,0) 100%);
  }
  .rule--top { top: 67px; }
  .rule--bottom { top: 193px; }
  .product-name {
    position: absolute;
    left: 0;
    top: 88px;
    width: 100%;
    text-align: center;
    font-family: "PT Serif", serif;
  }
  .product-name__main {
    display: block;
    color: var(--rose);
    font-weight: 700;
    font-size: 46px;
    line-height: 50px;
    letter-spacing: 0.5px;
  }
  .product-name__sub {
    display: block;
    color: var(--ink);
    font-weight: 400;
    font-size: 47px;
    line-height: 50px;
    letter-spacing: 0.5px;
  }
  .benefit {
    position: absolute;
    left: 0;
    top: 263px;
    width: 100%;
    text-align: center;
    font-family: "Josefin Sans", sans-serif;
    font-weight: 300;
    font-size: 26px;
    line-height: 40px;
    letter-spacing: 1px;
    color: var(--ink);
  }
  .accent-bar {
    position: absolute;
    left: 46px;
    top: 453px;
    width: 110px;
    height: 9px;
    background: linear-gradient(90deg, var(--rose) 0%, rgba(208,111,163,0.45) 45%, rgba(208,111,163,0) 100%);
  }
  .headline {
    position: absolute;
    left: 46px;
    top: 471px;
    font-family: "Oswald", sans-serif;
    font-weight: 600;
    font-size: 47px;
    line-height: 60px;
    color: var(--coral);
    text-transform: uppercase;
  }
  .volume {
    position: absolute;
    left: 46px;
    top: 690px;
    font-family: "Josefin Sans", sans-serif;
    font-weight: 400;
    font-size: 26px;
    color: var(--ink);
  }
  .swoosh {
    position: absolute;
    left: 0;
    top: 0;
    width: 471px;
    height: 808px;
  }
</style>
</head>
<body>
  <main class="label">
    <svg class="swoosh" viewBox="0 0 471 808" aria-hidden="true">
      <path fill="var(--peach-fill)" d="M0,743 C60,765 110,773 170,773 C300,773 410,700 471,601 L471,808 L0,808 Z"/>
      <path fill="var(--peach-band)" d="M170,773 C320,770 420,680 471,572 L471,601 C410,700 300,773 170,773 Z"/>
      <path fill="var(--rose)" d="M0,729 C70,750 150,760 230,758 Q270,752 298,737 C260,760 220,772 160,773 C100,773 50,763 0,743 Z"/>
    </svg>

    <div class="rule rule--top"></div>
    <h1 class="product-name">
      <span class="product-name__main">AFTER TATTOO</span>
      <span class="product-name__sub">&amp; PIERCING</span>
    </h1>
    <div class="rule rule--bottom"></div>

    <p class="benefit">Reduces inflammation,<br>irritation and encourages<br>natural skin healing</p>

    <div class="accent-bar"></div>
    <h2 class="headline">Expert skin repair<br>for new tattoos<br>&amp; piercings</h2>

    <p class="volume">100 mL</p>
  </main>
</body>
</html>
```